Geschäftspapiere für Hotel
Zielgruppe
Wir sind ein kleines Hotel mit 50 Zimmern, es nennt sich 'Stille Quelle'. Unsere Kunden sind sowohl Geschäfttsreisende, als auch Touristen

```html
<!DOCTYPE html>
<html lang="de">
<head>
<meta charset="utf-8">
<title>Stille Quelle – Briefbogen</title>
<link href="https://fonts.googleapis.com/css2?family=Montserrat:wght@400;500;600&display=swap" rel="stylesheet">
<style>
  :root {
    --canvas: #f2f2f2;
    --paper: #ffffff;
    --green: #8aa82b;
    --orange: #e06a00;
    --grey: #8c8c8c;
    --white: #ffffff;
  }
  * { box-sizing: border-box; margin: 0; padding: 0; }
  html, body {
    width: 965px; height: 1200px; overflow: hidden;
    background: var(--canvas);
    font-family: "Montserrat", sans-serif;
  }
  .sheet-holder {
    position: absolute; left: 58px; top: 0;
    width: 906px; height: 1282px;
    transform: scale(0.936); transform-origin: 0 0;
  }
  .letterhead {
    position: relative; width: 906px; height: 1282px;
    background: var(--paper); overflow: hidden;
  }
  .top-bar {
    position: absolute; left: 0; top: 0; width: 100%; height: 16px;
    background: var(--green);
  }
  .brand-name {
    position: absolute; right: 48px; top: 126px;
    font-size: 38px; font-weight: 500; color: var(--orange);
    letter-spacing: -0.5px; line-height: 1;
  }
  .sender-line {
    position: absolute; left: 116px; top: 196px;
    font-size: 8.5px; font-weight: 500; color: var(--grey);
  }
  .sender-line .sender-name { color: var(--orange); font-weight: 600; }
  .sender-line .dot { color: var(--orange); margin: 0 3px; }
  .contact-list {
    position: absolute; left: 694px; top: 208px; list-style: none;
  }
  .contact-list li {
    display: flex; align-items: center; height: 23.5px;
    font-size: 13.5px; color: var(--grey);
  }
  .contact-icon {
    width: 20px; height: 20px; border-radius: 50%;
    background: var(--orange); margin-right: 6px; flex: none;
    display: flex; align-items: center; justify-content: center;
  }
  .fold-mark {
    position: absolute; left: 10px; width: 10px; height: 2px;
    background: var(--orange);
  }
  .fold-mark.first { top: 452px; }
  .fold-mark.second { top: 905px; }
  .footer-band {
    position: absolute; left: 214px; right: 0; top: 1189px; bottom: 0;
    background: var(--orange);
  }
  .footer-col {
    position: absolute; top: 1209px;
    font-size: 11px; font-weight: 600; color: var(--white); line-height: 19px;
    white-space: nowrap;
  }
  .footer-col.address { left: 260px; }
  .footer-col.management { left: 458px; }
  .footer-col.bank { left: 646px; }
</style>
</head>
<body>
<div class="sheet-holder">
  <div class="letterhead">
    <div class="top-bar"></div>

    <div class="brand-name">Stille Quelle</div>

    <p class="sender-line"><span class="sender-name">Hotel Stille Quelle</span><span class="dot">·</span>Musterstrasse 1<span class="dot">·</span>12345 Musterstadt</p>

    <ul class="contact-list">
      <li><span class="contact-icon"><svg width="12" height="12" viewBox="0 0 12 12"><path d="M2.5 1 L4.5 1 L5.2 3.5 L4 4.5 C4.7 6 6 7.3 7.5 8 L8.5 6.8 L11 7.5 L11 9.5 C11 10.3 10.3 11 9.5 11 C5 11 1 7 1 2.5 C1 1.7 1.7 1 2.5 1 Z" fill="#fff"/></svg></span>0 00 00 / 0 00 00 00</li>
      <li><span class="contact-icon"><svg width="12" height="12" viewBox="0 0 12 12" fill="none" stroke="#fff" stroke-width="1.2"><rect x="3.5" y="1" width="5" height="3"/><rect x="1.5" y="4" width="9" height="4.5"/><rect x="3.5" y="7" width="5" height="4" fill="#e06a00"/></svg></span>0 00 00 / 0 00 00 01</li>
      <li><span class="contact-icon"><svg width="12" height="12" viewBox="0 0 12 12" fill="none" stroke="#fff" stroke-width="1.2"><rect x="1.5" y="3" width="9" height="6.5"/><path d="M1.5 3 L6 7 L10.5 3"/></svg></span>info@stille-quelle.de</li>
      <li><span class="contact-icon"><svg width="12" height="12" viewBox="0 0 12 12" fill="none" stroke="#fff" stroke-width="1"><circle cx="6" cy="6" r="4.8"/><ellipse cx="6" cy="6" rx="2.2" ry="4.8"/><path d="M1.2 6 H10.8 M2 3.5 H10 M2 8.5 H10"/></svg></span>www.stille-quelle.de</li>
    </ul>

    <div class="fold-mark first"></div>
    <div class="fold-mark second"></div>

    <div class="footer-band"></div>
    <div class="footer-col address">Hotel Stille Quelle<br>Musterstrasse 1<br>12345 Musterstadt</div>
    <div class="footer-col management">Max Mustermann<br>Geschäftsführer<br>St.Nr.: 000/0000/0000</div>
    <div class="footer-col bank">Musterbank Musterstadt<br>IBAN DE00 0000 0000 0000 0000 00<br>BIC MUSTDEXX000</div>
  </div>
</div>
</body>
</html>
```